www.belvunit.com

Website design for IT outsourcing company (Belvun IT)
Pages: Home, About Us, Services, Case Studies, Careers, Contact and more (see current website for guidance)
Include client testimonials
Include client logos (e.g., Dulvane, etc)
List of services (staffing, app dev, integration, cloud)
Modern, clean, professional design
Blue/white/gray color scheme
Mobile and desktop responsive
Include call-to-action buttons
Space for case studies/project highlights

```html
<!DOCTYPE html>
<html lang="en">
<head>
<meta charset="utf-8">
<title>Belvun IT</title>
<link href="https://fonts.googleapis.com/css2?family=Montserrat:wght@400;500;600;700;800&display=swap" rel="stylesheet">
<style>
:root{
  --navy:#13307a;
  --navy-dark:#0b1c4f;
  --ink:#111827;
  --text:#4a4f5c;
  --muted:#6b7080;
  --gray-bg:#e3e6ec;
  --sky:#c6d7e6;
  --white:#ffffff;
  --black:#050505;
}
*{box-sizing:border-box;margin:0;padding:0}
html,body{width:1200px;height:4878px;overflow:hidden}
body{position:relative;font-family:'Montserrat',sans-serif;color:var(--ink);background:var(--white)}
.abs{position:absolute}
.ph{position:absolute}
svg{display:block}

/* top bar + nav */
.topbar{left:284px;top:0;width:916px;height:42px;background:var(--navy);color:#fff;font-size:13px;display:flex;align-items:center;gap:22px;padding-left:34px}
.topbar .sep{opacity:.7}
.topbar span{display:flex;align-items:center;gap:7px}
.brand-tab{left:92px;top:0;width:166px;height:132px;background:#fff;z-index:3;display:flex;align-items:flex-end;justify-content:center;padding-bottom:16px}
.brand-tab .name{font-weight:800;font-size:20px;color:var(--navy);letter-spacing:.5px;display:flex;align-items:center;gap:8px}
.brand-tab .sq{width:14px;height:14px;background:var(--navy)}
.nav{left:320px;top:42px;width:800px;height:62px;display:flex;align-items:center;justify-content:space-between;font-size:17px;font-weight:500}
.nav a{color:var(--ink);text-decoration:none}
.nav a.active{color:var(--navy)}
.nav-rule{left:0;top:102px;width:1200px;height:2px;background:#dfe3ea}

/* hero */
.hero{left:0;top:104px;width:1200px;height:611px;background:linear-gradient(110deg,#070d22 0%,#142b6b 45%,#0b1535 100%);overflow:hidden}
.hero h1{position:absolute;left:95px;top:126px;color:#fff;font-size:30px;font-weight:500;line-height:43px;letter-spacing:.3px}
.hero h1 b{font-weight:700}
.hero p{position:absolute;left:97px;top:272px;color:#e6eaf4;font-size:16px;line-height:25px}
.btn{display:inline-block;background:var(--navy);color:#fff;font-weight:600;font-size:16px;padding:11px 44px 11px 22px;clip-path:polygon(0 0,100% 0,88% 100%,0 100%)}
.hero .btn{position:absolute;left:95px;top:354px;background:#1d3f93}
.hero-photo{left:757px;top:28px;width:379px;height:583px;background:linear-gradient(180deg,#c98a1f 0%,#d9a23a 50%,#2f4b7a 100%);border-radius:190px 190px 0 0}
.hero-edge{left:0;top:560px}
.scroll-badge{left:567px;top:620px}

/* section headings */
.head{position:absolute;left:0;width:1200px;text-align:center}
.head .mark{width:34px;height:5px;background:var(--navy);margin:0 auto 14px}
.head h2{font-size:41px;font-weight:500;letter-spacing:.5px;color:var(--ink)}
.head h2 b{font-weight:700}
.head p{margin-top:12px;font-size:14.5px;line-height:25px;color:var(--muted)}

/* services */
.svc{position:absolute;top:962px;width:238px;height:306px}
.svc .img{position:absolute;left:0;top:0;width:238px;height:260px}
.svc .label{position:absolute;left:12px;top:258px;width:214px;height:48px;background:#fff;box-shadow:0 4px 10px rgba(0,0,0,.12);display:flex;align-items:center;justify-content:space-between;padding:0 12px 0 18px;font-weight:600;font-size:16px}
.arrow-dot{width:30px;height:30px;border-radius:50%;background:#8da4c9;display:flex;align-items:center;justify-content:center}
.arrow-dot.on{background:var(--navy)}

/* about */
.about{left:0;top:1353px;width:1200px;height:811px;background:linear-gradient(90deg,#c9ced8 0%,#e9ebef 50%,#c7ccd6 100%);overflow:hidden}
.about .copy{position:absolute;left:600px;top:130px;width:460px}
.about h2{font-size:41px;font-weight:500}
.about h2 b{font-weight:700}
.about p{font-size:16px;line-height:30px;color:#3a3f4b;margin-top:22px}
.about h3{font-size:24px;font-weight:500;margin-top:22px;margin-left:-3px}
.about .btn{margin-top:26px}

/* testimonials */
.tcard{position:absolute;width:303px;background:#fff;border-radius:26px;box-shadow:0 6px 18px rgba(0,0,0,.12);text-align:center;padding-top:80px}
.tcard.feature{background:var(--navy);color:#fff}
.tcard .avatar{position:absolute;left:100px;top:-52px;width:104px;height:104px;border-radius:50%;border:4px solid #fff;background:linear-gradient(160deg,#a8b3c4,#55607a)}
.tcard h4{font-size:28px;font-weight:500}
.tcard .role{font-size:19px;margin-top:4px}
.tcard .quote{font-size:46px;font-weight:800;line-height:40px;margin-top:20px;font-family:Georgia,serif}
.tcard p{font-size:13.5px;line-height:21px;padding:14px 20px 28px;color:#666}
.tcard.feature p{color:#e3e8f5}

/* case studies */
.cases{left:0;top:3057px;width:1200px;height:814px;background:linear-gradient(180deg,#b9cde0 0%,#c9d9e7 100%);overflow:hidden}
.case-card{left:496px;top:388px;width:547px;height:383px;background:#fff;padding:40px 0 0 100px}
.case-card h3{font-size:29px;font-weight:600;color:var(--navy)}
.case-card .meta{font-size:14.5px;font-weight:600;margin-top:12px}
.case-card p{font-size:16px;line-height:26px;color:#3a3f4b;margin-top:20px;width:410px}
.case-photo{left:163px;top:333px;width:397px;height:385px;background:linear-gradient(120deg,#2e3a4c 0%,#8a6a4a 45%,#3b4f6e 100%)}

/* brands */
.brand{position:absolute;top:4142px;width:240px;height:91px;background:#fff;border-radius:12px;box-shadow:0 4px 12px rgba(0,0,0,.12);display:flex;align-items:center;justify-content:center;font-size:32px;font-weight:600;color:#1e2330}
.dots{left:550px;top:4257px;display:flex;gap:8px}
.dots i{width:19px;height:19px;border-radius:50%;border:2px solid #6b7894;display:block}
.dots i.on{background:var(--navy);border-color:var(--navy)}

/* footer */
.footer{left:0;top:4325px;width:1200px;height:553px;background:var(--black);color:#fff;overflow:hidden}
.footer .logo{position:absolute;left:110px;top:300px;font-size:46px;font-weight:800;letter-spacing:1px;display:flex;align-items:center;gap:14px}
.footer .logo .sq{width:26px;height:26px;background:#fff}
.fcol{position:absolute;top:160px}
.fcol h5{font-size:25px;font-weight:600}
.fcol .bar{width:50px;height:4px;background:var(--navy);margin:16px 0 22px}
.fcol ul{list-style:none;font-size:17px;line-height:30px}
.fcol .line{display:flex;gap:10px;font-size:17px;line-height:28px;margin-bottom:18px}
.copyright{position:absolute;left:112px;top:488px;width:975px;display:flex;justify-content:space-between;font-size:16px}
</style>
</head>
<body>

<!-- header -->
<div class="abs brand-tab"><span class="name"><span class="sq"></span>BELVUN IT</span></div>
<div class="abs topbar">
  <span><svg width="14" height="11" viewBox="0 0 14 11"><rect x="1" y="1" width="12" height="9" fill="none" stroke="#fff" stroke-width="1.4"/><path d="M1 1l6 5 6-5" fill="none" stroke="#fff" stroke-width="1.4"/></svg>admin@belvunit.com</span>
  <span class="sep">|</span>
  <span><svg width="10" height="13" viewBox="0 0 10 13"><path d="M5 0a5 5 0 0 1 5 5c0 4-5 8-5 8S0 9 0 5a5 5 0 0 1 5-5z" fill="#fff"/><circle cx="5" cy="5" r="2" fill="#13307a"/></svg>Marven Street, Kestrel Park (Orla Bank Building)</span>
  <span class="sep">|</span>
  <span><svg width="13" height="13" viewBox="0 0 13 13"><circle cx="6.5" cy="6.5" r="5.5" fill="none" stroke="#fff" stroke-width="1.4"/><path d="M6.5 3v4h3" fill="none" stroke="#fff" stroke-width="1.4"/></svg>Mon - Fri 8:30 AM to 5:30 PM</span>
</div>
<nav class="abs nav">
  <a class="active" href="#">&#9670; Home</a><a href="#">About Us</a><a href="#">Services</a><a href="#">Case Studies</a><a href="#">Careers</a><a href="#">Contact</a>
</nav>
<div class="abs nav-rule"></div>

<!-- hero -->
<section class="abs hero">
  <div class="ph hero-photo" role="img" aria-label="Smiling professional in a mustard shirt holding an open laptop"></div>
  <h1>SPEED UP <b>THE PROCESS</b> OF<br><b>DEVELOPING YOUR SOFTWARE</b><br>WITH <b>CONFIDENCE</b></h1>
  <p>Our focus is to create amazing software and<br>establish successful software firms</p>
  <a class="btn">Get in Touch</a>
</section>
<svg class="abs hero-edge" width="1200" height="160" viewBox="0 0 1200 160">
  <polygon points="0,55 1200,95 1200,160 0,160" fill="#fff"/>
  <polygon points="0,55 520,72 0,155" fill="#13307a"/>
</svg>
<svg class="abs scroll-badge" width="62" height="70" viewBox="0 0 62 70">
  <polygon points="31,2 60,18 60,52 31,68 2,52 2,18" fill="#1d3f93" stroke="#fff" stroke-width="2"/>
  <path d="M21 26l10 9 10-9M21 36l10 9 10-9" fill="none" stroke="#fff" stroke-width="2.5"/>
</svg>

<!-- services -->
<div class="head" style="top:790px">
  <div class="mark"></div>
  <h2>OUR <b>SERVICES</b></h2>
  <p>Lorem ipsum dolor sit amet, consectetur adipiscing elit, sed do eiusmod tempor<br>incididunt ut labore et dolore magna aliqua.</p>
</div>
<div class="svc" style="left:110px"><div class="ph img" role="img" aria-label="Team collaborating around a laptop" style="background:linear-gradient(150deg,#bfc4c6,#5b5e61)"></div><div class="label">Staffing<span class="arrow-dot"><svg width="12" height="12" viewBox="0 0 12 12"><path d="M4 2l4 4-4 4" fill="none" stroke="#fff" stroke-width="2"/></svg></span></div></div>
<div class="svc" style="left:356px"><div class="ph img" role="img" aria-label="Developer typing code on a laptop" style="background:linear-gradient(150deg,#2f4658,#0f1a24)"></div><div class="label">App Dev<span class="arrow-dot on"><svg width="12" height="12" viewBox="0 0 12 12"><path d="M4 2l4 4-4 4" fill="none" stroke="#fff" stroke-width="2"/></svg></span></div></div>
<div class="svc" style="left:602px"><div class="ph img" role="img" aria-label="Glowing network of connected technology icons" style="background:linear-gradient(150deg,#1a3f86,#0a1740)"></div><div class="label">Integration<span class="arrow-dot"><svg width="12" height="12" viewBox="0 0 12 12"><path d="M4 2l4 4-4 4" fill="none" stroke="#fff" stroke-width="2"/></svg></span></div></div>
<div class="svc" style="left:848px"><div class="ph img" role="img" aria-label="Engineers walking through a server room" style="background:linear-gradient(150deg,#1f4f95,#0b1f48)"></div><div class="label">Cloud<span class="arrow-dot"><svg width="12" height="12" viewBox="0 0 12 12"><path d="M4 2l4 4-4 4" fill="none" stroke="#fff" stroke-width="2"/></svg></span></div></div>

<!-- about -->
<section class="abs about">
  <svg class="abs" style="left:0;top:0" width="1200" height="811" viewBox="0 0 1200 811">
    <polygon points="580,60 1200,0 1200,105" fill="#13307a"/>
    <polygon points="0,110 0,360 30,110" fill="#13307a"/>
    <polygon points="55,90 80,90 80,330" fill="#13307a"/>
    <polygon points="0,811 60,690 135,811" fill="#13307a"/>
    <polygon points="300,811 420,700 490,811" fill="#13307a"/>
  </svg>
  <div class="ph" role="img" aria-label="Network cables and gears over a server panel" style="left:119px;top:131px;width:379px;height:303px;background:linear-gradient(140deg,#1c2e22,#8d9ab0 60%,#2c3e5c)"></div>
  <div class="ph" role="img" aria-label="Hand reaching toward a glowing circuit board" style="left:0;top:404px;width:299px;height:270px;background:linear-gradient(140deg,#08152e,#1c3f7a)"></div>
  <div class="ph" role="img" aria-label="Futuristic city of data towers" style="left:324px;top:498px;width:196px;height:231px;background:linear-gradient(160deg,#0c1d3b,#c48a3d 70%,#14284d)"></div>
  <div class="copy">
    <div style="width:34px;height:5px;background:var(--navy);margin-bottom:18px"></div>
    <h2>ABOUT <b>BELVUN IT</b></h2>
    <p>Our approach as a software development partner is distinct, as we prioritize collaboration and teamwork with our clients to deliver cutting-edge solutions. We will be there to assist in every aspect, starting from the conception of ideas to their execution.</p>
    <h3>Our Mission</h3>
    <p style="margin-top:12px">As an innovative technology group, we are committed to adopting a consistent and persistent approach that ensures our success while inspiring our partners and clients.</p>
    <a class="btn">Read More</a>
  </div>
</section>

<!-- testimonials -->
<div class="head" style="top:2278px">
  <div class="mark"></div>
  <h2>CLIENT <b>TESTIMONIALS</b></h2>
  <p>Lorem ipsum dolor sit amet, consectetur adipiscing elit, sed do eiusmod tempor<br>incididunt ut labore et dolore magna aliqua.</p>
</div>
<div class="tcard" style="left:110px;top:2559px;height:386px">
  <div class="ph avatar" role="img" aria-label="Client portrait"></div>
  <h4>Pell Marrow</h4><div class="role">Staff</div><div class="quote">&#8221;</div>
  <p>Sed ut perspiciatis unde omnis iste natus error sit voluptatem accusantium doloremque laudantium, totam rem aperiam, eaque ipsa quae ab illo inventore veritatis et quasi architecto beatae vitae dicta sunt explicabo. Nemo enim ipsam voluptatem</p>
</div>
<div class="tcard feature" style="left:443px;top:2512px;height:384px">
  <div class="ph avatar" role="img" aria-label="Client portrait"></div>
  <h4>Toren Vale</h4><div class="role">Staff</div><div class="quote">&#8221;</div>
  <p>Sed ut perspiciatis unde omnis iste natus error sit voluptatem accusantium doloremque laudantium, totam rem aperiam, eaque ipsa quae ab illo inventore veritatis et quasi architecto beatae vitae dicta sunt explicabo. Nemo enim ipsam voluptatem</p>
</div>
<div class="tcard" style="left:773px;top:2559px;height:386px">
  <div class="ph avatar" role="img" aria-label="Client portrait"></div>
  <h4>Ansel Grey</h4><div class="role">Staff</div><div class="quote">&#8221;</div>
  <p>Sed ut perspiciatis unde omnis iste natus error sit voluptatem accusantium doloremque laudantium, totam rem aperiam, eaque ipsa quae ab illo inventore veritatis et quasi architecto beatae vitae dicta sunt explicabo. Nemo enim ipsam voluptatem</p>
</div>

<!-- case studies -->
<section class="abs cases">
  <svg class="abs" style="left:0;top:0" width="1200" height="120" viewBox="0 0 1200 120">
    <polygon points="0,0 1200,0 1200,10 0,105" fill="#13307a"/>
  </svg>
  <div class="head" style="top:150px">
    <div class="mark"></div>
    <h2>OUR <b>CASE STUDIES</b></h2>
    <p>Lorem ipsum dolor sit amet, consectetur adipiscing elit, sed do eiusmod tempor<br>incididunt ut labore et dolore magna aliqua.</p>
  </div>
  <div class="abs case-card">
    <h3>Belvun IT</h3>
    <div class="meta">Leave a Comment / Uncategorized / By admin</div>
    <p>Sed ut perspiciatis unde omnis iste natus error sit voluptatem accusantium doloremque laudantium, totam rem aperiam, eaque ipsa quae ab illo inventore veritatis et quasi architecto beatae vitae dicta sunt explicabo. Nemo enim ipsam voluptatem quia voluptas</p>
    <svg class="abs" style="left:365px;top:322px" width="150" height="42" viewBox="0 0 150 42">
      <circle cx="20" cy="21" r="19" fill="#b9cde0"/>
      <path d="M6 21h40M16 11L6 21l10 10" fill="none" stroke="#13307a" stroke-width="3"/>
      <circle cx="130" cy="21" r="19" fill="#b9cde0"/>
      <path d="M100 21h42M132 11l10 10-10 10" fill="none" stroke="#111" stroke-width="3"/>
    </svg>
  </div>
  <div class="ph case-photo" role="img" aria-label="Two colleagues discussing work over a laptop"></div>
</section>

<!-- brands -->
<div class="head" style="top:3962px">
  <div class="mark"></div>
  <h2>BRANDS <b>THAT TRUST US</b></h2>
  <p>Lorem ipsum dolor sit amet, consectetur adipiscing elit, sed do eiusmod tempor<br>incididunt ut labore et dolore magna aliqua.</p>
</div>
<div class="brand" style="left:108px">Paynora</div>
<div class="brand" style="left:354px">Hollisway</div>
<div class="brand" style="left:600px">Dulvane</div>
<div class="brand" style="left:846px">Marlstone</div>
<div class="abs dots"><i class="on"></i><i></i><i></i><i></i></div>

<!-- footer -->
<footer class="abs footer">
  <svg class="abs" style="left:0;top:0" width="1200" height="90" viewBox="0 0 1200 90">
    <polygon points="0,0 912,0 0,38" fill="#fff"/>
    <polygon points="540,20 912,0 912,80 540,80" fill="#13307a"/>
  </svg>
  <div class="logo"><span class="sq"></span>BELVUN IT</div>
  <div class="fcol" style="left:479px">
    <h5>QUICK LINKS</h5><div class="bar"></div>
    <ul><li>Home</li><li>About Us</li><li>Services</li><li>Case Studies</li><li>Careers</li><li>Contact</li></ul>
  </div>
  <div class="fcol" style="left:742px">
    <h5>CONTACT US</h5><div class="bar"></div>
    <div class="line"><svg width="11" height="14" viewBox="0 0 10 13" style="margin-top:6px"><path d="M5 0a5 5 0 0 1 5 5c0 4-5 8-5 8S0 9 0 5a5 5 0 0 1 5-5z" fill="#fff"/><circle cx="5" cy="5" r="2" fill="#000"/></svg><span>Marven Street, Kestrel Park (Orla<br>Bank Building)</span></div>
    <div class="line"><svg width="15" height="12" viewBox="0 0 14 11" style="margin-top:8px"><rect x="1" y="1" width="12" height="9" fill="none" stroke="#fff" stroke-width="1.4"/><path d="M1 1l6 5 6-5" fill="none" stroke="#fff" stroke-width="1.4"/></svg><span>admin@belvunit.com</span></div>
    <div class="line"><svg width="14" height="14" viewBox="0 0 13 13" style="margin-top:7px"><circle cx="6.5" cy="6.5" r="5.5" fill="none" stroke="#fff" stroke-width="1.4"/><path d="M6.5 3v4h3" fill="none" stroke="#fff" stroke-width="1.4"/></svg><span>Mon - Fri 8:30 AM to 5:30 PM</span></div>
  </div>
  <div class="copyright"><span>&copy; 2025 Belvun IT. All Rights Reserved.</span><span>Privacy policy &nbsp;/&nbsp; Terms &amp; conditions</span></div>
</footer>

</body>
</html>
```